Etiketten für Kürbiskernöl
Zielgruppe
Wir betreiben eine Landwirschaft, vorwiegend Ackerbau und Viehwirtschaft im nordöstlichen Niederösterreich. Wir sind ein reines Familienunternehmen. Unsere Zielgruppe ist 20 Jahre aufwärts, männlich wie weiblich und legt großen Wert auf Regionalität und hohe Qualität der Produkte.
Aufgabenstellung
Das Etikett wird für unsere Kürbiskernölflasche benötigt. Die Vorderseite soll unseren Namen, Produktbezeichnung und Füllmenge enthalten. Familie Wendtner - Kürbiskernöl 100% rein - 500ml Für die Rückseite gibt es einen entsprechenden Text (siehe Anhang).
Angehängt haben wir auch Etikett Vorderseiten, die uns sehr ansprechen. Es soll auf jeden Fall ein Kürbis abgebildet sein und ein hochwertiges, eher minimalistischen Design haben.
In Zukunft könnten wir uns auch vorstellen die Kürbiskerne in Form von Knabberkernen zu verkaufen, wofür wir das Etikettendesign gern abwandeln würden.
Farben: dunkelgrau/schwarz, weiß, dunkelgrün/oliv, beige
Flaschenform: Valmera 500ml siehe Foto

```html
<!DOCTYPE html>
<html lang="de">
<head>
<meta charset="utf-8">
<title>Kürbiskernöl Etiketten – Familie Wendtner</title>
<link href="https://fonts.googleapis.com/css2?family=Amatic+SC:wght@400;700&family=Montserrat:wght@400;500;600&display=swap" rel="stylesheet">
<style>
  :root {
    --canvas: #ffffff;
    --label: #1f1f1e;
    --olive: #a4ad6a;
    --olive-text: #a8b16c;
    --ink: #f4f3ee;
    --art-dark: #262625;
    --art-light: #3b3b38;
  }
  * { margin: 0; padding: 0; box-sizing: border-box; }
  html, body {
    width: 1200px; height: 600px; overflow: hidden;
    background: var(--canvas);
  }
  .canvas { position: relative; width: 1200px; height: 600px; }

  .label {
    position: absolute; top: 20px; width: 190px; height: 560px;
    background: var(--label); color: var(--ink);
    font-family: "Montserrat", sans-serif;
    border-top: 10px solid var(--olive);
    border-bottom: 10px solid var(--olive);
  }
  .label--back { left: 400px; }
  .label--front { left: 610px; }

  .back-copy {
    position: absolute; left: 18px; right: 17px;
    font-size: 7.6px; line-height: 1.33; text-align: justify;
  }
  .back-copy--intro { top: 17px; }
  .back-copy--process { top: 110px; }
  .back-claim {
    position: absolute; left: 0; right: 0; top: 72px;
    text-align: center; color: var(--olive-text);
    font-family: "Amatic SC", cursive; font-size: 14px; letter-spacing: .3px;
  }
  .back-info {
    position: absolute; left: 18px; right: 10px;
    font-size: 7.6px; line-height: 1.4;
  }
  .back-info--address { top: 325px; }
  .back-info--storage { top: 358px; }
  .back-info--date { top: 374px; display: flex; align-items: baseline; gap: 10px; }
  .back-info--date .date {
    font-family: "Amatic SC", cursive; font-size: 12px; letter-spacing: .4px;
  }
  .back-volume {
    position: absolute; right: 13px; bottom: 4px;
    font-family: "Amatic SC", cursive; font-size: 20px; letter-spacing: .5px;
  }

  .front-family {
    position: absolute; left: 0; right: 0; top: 20px; text-align: center;
  }
  .front-family .family-word {
    display: block; font-size: 9px; letter-spacing: 3.2px; font-weight: 500;
    padding-left: 3px;
  }
  .front-family .family-name {
    display: block; font-family: "Amatic SC", cursive; font-size: 16px;
    letter-spacing: .6px; margin-top: 1px;
  }
  .product-name {
    position: absolute; left: 0; right: 0; top: 140px; text-align: center;
    font-family: "Amatic SC", cursive; font-weight: 400;
    font-size: 58px; line-height: .92; letter-spacing: 1px;
  }
  .product-rule {
    position: absolute; left: 60px; width: 70px; top: 255px;
    height: 2px; background: var(--olive); border-radius: 1px;
  }
  .product-purity {
    position: absolute; left: 0; right: 0; top: 266px; text-align: center;
    font-size: 8px; letter-spacing: 3px; font-weight: 500; padding-left: 3px;
  }
  .front-method {
    position: absolute; left: 0; right: 0; bottom: 9px; text-align: center;
    font-size: 6.6px; letter-spacing: 1.4px; font-weight: 600;
  }

  .pumpkin-art {
    position: absolute; border-radius: 40% 40% 30% 30%;
    background: radial-gradient(ellipse at 45% 50%, var(--art-light), var(--art-dark) 70%, var(--label));
  }
  .pumpkin-art--back { left: 4px; top: 400px; width: 122px; height: 130px; }
  .pumpkin-art--front { left: 6px; top: 395px; width: 178px; height: 130px; }
</style>
</head>
<body>
<main class="canvas">

  <section class="label label--back" aria-label="Rückseite">
    <p class="back-copy back-copy--intro">Nur die besten Kürbiskerne aus unserem eigenen Anbau werden zu unserem g'sund, g'schmackig, guatem Kürbiskernöl verarbeitet.</p>
    <p class="back-claim">100% rein und naturbelassen</p>
    <p class="back-copy back-copy--process">Die Kürbiskerne werden schonend geröstet und in einem traditionellen Verfahren in einer regionalen Ölmühle kalt gepresst, was unserem Kürbiskernöl das einzigartige, intensiv-nussige Aroma verleiht.</p>
    <p class="back-info back-info--address">Familie Wendtner<br>2071 Lindenau 14</p>
    <p class="back-info back-info--storage">Vor Wärme und Licht geschützt lagern.</p>
    <p class="back-info back-info--date"><span>Mindestens haltbar bis:</span><span class="date">OKTOBER 2022</span></p>
    <div class="pumpkin-art pumpkin-art--back" role="img" aria-label="Weiße Strichzeichnung eines Kürbisses"></div>
    <p class="back-volume">500 ML</p>
  </section>

  <section class="label label--front" aria-label="Vorderseite">
    <p class="front-family"><span class="family-word">FAMILIE</span><span class="family-name">WENDTNER</span></p>
    <h1 class="product-name">KÜRBIS<br>KERNÖL</h1>
    <div class="product-rule"></div>
    <p class="product-purity">100% REIN</p>
    <div class="pumpkin-art pumpkin-art--front" role="img" aria-label="Weiße Strichzeichnung eines Kürbisses mit aufgeschnittenem Stück und Kernen"></div>
    <p class="front-method">TRADITIONELL KALTGEPRESST</p>
  </section>

</main>
</body>
</html>
```